Apricot Variety Sheet - Meadowlark Orchard Co

We are needing a variety sheet that we can hand out that will describe the different apricot vatieties we have available. The attached document has the name of the variety along with a description that will need to be on the sheet. We are looking for a modern, appealing way to display this information on 1 page (if needed, it can be front and back)
Updates

Apologies for the delay; we are overwhelmed with the great design options and will be sorting through them all (across our contests) to pick a collective. Thank you for your patience.

Target Market(s)

Growers and consumers

Industry/Entity Type

Agriculture

Requirements
Must have
• Easy to read
• Natural color palettes to emphasize the agricultural nature
• Clearly show washington as the origin in the title or at the top
Nice to have
• incorporate Apricots in the design

```html
<!DOCTYPE html>
<html lang="en">
<head>
<meta charset="utf-8">
<title>Washington Apricot Variety Sheet – Meadowlark Orchard Co</title>
<link rel="stylesheet" href="https://fonts.googleapis.com/css2?family=Lobster&family=Raleway:wght@300;400;600;800&display=swap">
<style>
  :root {
    --backdrop: #ededed;
    --paper: #ffffff;
    --apricot-light: #ffc24a;
    --apricot: #f9a425;
    --apricot-deep: #ef7f12;
    --title-shadow: #d9670c;
    --fruit-light: #ffc163;
    --fruit-mid: #f68b3a;
    --fruit-deep: #e0532c;
    --leaf: #5f9e2f;
    --leaf-dark: #3d7a22;
    --brand-green: #2f7a34;
    --ink: #6b6b6b;
    --stripe-orange: #f29a3a;
    --stripe-red: #d6544a;
    --stripe-lime: #b8cc4c;
    --stripe-green: #5aa33a;
  }
  * { box-sizing: border-box; margin: 0; padding: 0; }
  html, body { width: 1200px; height: 960px; overflow: hidden; }
  body { background: var(--backdrop); position: relative; font-family: "Raleway", sans-serif; }

  .sheet {
    position: absolute;
    top: 82px;
    width: 500px;
    height: 796px;
    background: var(--paper);
    overflow: hidden;
    box-shadow: 0 6px 18px rgba(0,0,0,0.12);
  }
  .sheet--front { left: 70px; }
  .sheet--back { left: 630px; }

  /* Front */
  .front-wash { position: absolute; left: 0; top: 0; width: 500px; height: 680px; }
  .front-title { position: absolute; top: 20px; left: 0; width: 100%; text-align: center; color: #fff; font-weight: 400; }
  .front-title__origin {
    display: block;
    font-weight: 800;
    font-size: 17px;
    letter-spacing: 5px;
    line-height: 1;
    margin-bottom: 14px;
  }
  .front-title__script {
    display: block;
    font-family: "Lobster", cursive;
    font-size: 100px;
    line-height: 1;
    transform: rotate(-4deg);
    text-shadow: 4px 5px 0 var(--title-shadow);
  }
  .front-title__sub {
    display: block;
    margin-top: 4px;
    font-weight: 300;
    font-size: 48px;
    letter-spacing: 1px;
    line-height: 1.1;
  }
  .hero-fruit {
    position: absolute;
    left: 40px; top: 262px;
    width: 420px; height: 355px;
    border-radius: 48% 52% 46% 54% / 50% 48% 52% 50%;
    background: radial-gradient(circle at 40% 38%, var(--fruit-light) 0%, var(--fruit-mid) 55%, var(--fruit-deep) 100%);
  }
  .brand {
    position: absolute;
    left: 0; top: 702px; width: 100%;
    display: flex; align-items: center; justify-content: center; gap: 12px;
  }
  .brand__dot { width: 42px; height: 42px; border-radius: 50%; background: var(--brand-green); }
  .brand__name { font-weight: 800; font-size: 22px; color: var(--brand-green); }
  .color-stripe { position: absolute; left: 0; bottom: 0; width: 100%; height: 9px; display: flex; }
  .color-stripe span { flex: 1; }
  .color-stripe .s1 { background: var(--stripe-orange); }
  .color-stripe .s2 { background: var(--stripe-red); }
  .color-stripe .s3 { background: var(--stripe-lime); }
  .color-stripe .s4 { background: var(--stripe-green); }

  /* Back */
  .back-band { position: absolute; left: 0; width: 500px; }
  .back-band--top { top: 0; height: 130px; }
  .back-band--bottom { bottom: 0; height: 160px; }
  .leaf-cluster {
    position: absolute; top: -10px;
    width: 90px; height: 70px;
    border-radius: 50% 10% 50% 10%;
    background: linear-gradient(135deg, var(--leaf) 0%, var(--leaf-dark) 100%);
  }
  .leaf-cluster--left { left: -14px; }
  .leaf-cluster--right { right: -14px; border-radius: 10% 50% 10% 50%; }
  .varieties {
    position: absolute;
    left: 34px; top: 146px;
    width: 432px;
    display: grid;
    grid-template-columns: 1fr 1fr;
    column-gap: 26px;
  }
  .variety { font-size: 10.4px; line-height: 1.45; color: var(--ink); margin-bottom: 12px; }
  .variety__name { font-weight: 800; color: var(--apricot-deep); text-transform: uppercase; }
  .corner-fruit {
    position: absolute;
    right: 26px; bottom: 22px;
    width: 190px; height: 175px;
    border-radius: 50%;
    background: radial-gradient(circle at 42% 40%, var(--fruit-light) 0%, var(--fruit-mid) 60%, var(--fruit-deep) 100%);
  }
</style>
</head>
<body>

  <section class="sheet sheet--front">
    <svg class="front-wash" viewBox="0 0 500 680" preserveAspectRatio="none" aria-hidden="true">
      <defs>
        <linearGradient id="washFront" x1="0" y1="0" x2="0.4" y2="1">
          <stop offset="0" stop-color="#f79a1e"/>
          <stop offset="0.5" stop-color="#fbb13a"/>
          <stop offset="1" stop-color="#ffc24a"/>
        </linearGradient>
      </defs>
      <path fill="url(#washFront)" d="M0 0H500V600C470 612 445 598 410 615C370 632 330 606 290 622C250 640 205 612 165 630C120 650 85 620 45 636C25 644 10 634 0 640Z"/>
    </svg>

    <h1 class="front-title">
      <span class="front-title__origin">WASHINGTON GROWN</span>
      <span class="front-title__script">Apricot</span>
      <span class="front-title__sub">VARIETY SHEET</span>
    </h1>

    <div class="hero-fruit" role="img" aria-label="Illustration of two whole apricots with a leaf and a halved apricot showing its stone"></div>

    <div class="brand">
      <span class="brand__dot"></span>
      <span class="brand__name">Meadowlark Orchard Co</span>
    </div>

    <div class="color-stripe"><span class="s1"></span><span class="s2"></span><span class="s3"></span><span class="s4"></span></div>
  </section>

  <section class="sheet sheet--back">
    <svg class="back-band back-band--top" viewBox="0 0 500 130" preserveAspectRatio="none" aria-hidden="true">
      <defs>
        <linearGradient id="washTop" x1="0" y1="0" x2="1" y2="0">
          <stop offset="0" stop-color="#f79a1e"/>
          <stop offset="1" stop-color="#ffbe45"/>
        </linearGradient>
      </defs>
      <path fill="url(#washTop)" d="M0 0H500V92C470 100 450 88 420 98C390 108 360 94 330 104C300 112 270 98 240 108C205 118 175 102 145 110C110 118 80 100 50 112C30 120 14 108 0 114Z"/>
    </svg>
    <div class="leaf-cluster leaf-cluster--left" role="img" aria-label="Apricot leaves"></div>
    <div class="leaf-cluster leaf-cluster--right" role="img" aria-label="Apricot leaves"></div>

    <div class="varieties">
      <div class="variety-col">
        <p class="variety"><span class="variety__name">Rival</span> – Great flavor with a fine, firm texture distinguishes this large oval apricot. The skin is light orange with a red blush. Available early July to early August.</p>
        <p class="variety"><span class="variety__name">Robada</span> – This jumbo apricot has a delicious floral flavor with a firm texture. Bright orange with a deep red blush. Available early June.</p>
        <p class="variety"><span class="variety__name">Perfection</span> – This classic large oval apricot is deep orange with an oblong shape and firm texture. Very sweet and full of flavor. Available mid July to mid August.</p>
        <p class="variety"><span class="variety__name">Patterson</span> – This apricot has a well balanced flavor and an excellent shelf life. Perfect for canning or drying. Available mid to late June.</p>
        <p class="variety"><span class="variety__name">Tomcot</span> – Tangy, sweet flavor with a firm texture. This oval apricot is light orange with a bright blush. Available late June to late July.</p>
        <p class="variety"><span class="variety__name">Goldrich</span> – This apricot is round with a bright orange skin and a deep orange flesh. A mild, sweet flavor with a firm texture. Available early July to mid August.</p>
      </div>
      <div class="variety-col">
        <p class="variety"><span class="variety__name">Castlebrite</span> – This medium sized apricot is golden orange with a slight red blush. Sweet and juicy, great for eating out of hand. Available late June.</p>
        <p class="variety"><span class="variety__name">Goldbar</span> – Moderately juicy, this large oval apricot has a light yellow orange skin with a reddish blush. The flesh is firm and meaty. Available late June to early July.</p>
        <p class="variety"><span class="variety__name">Sweet Jullet</span> – This special variety has a unique, sweet flavor with a juicy flesh. It is bright orange in color. Available through July.</p>
        <p class="variety"><span class="variety__name">Tasty Rich</span> – This early variety is light yellow orange colored with a firm texture. Very juicy with an enticing flavor. Available through June.</p>
        <p class="variety"><span class="variety__name">Goldstrike</span> – A large apricot with light orange, blushed skin. Firm texture with a slight tart taste until fully ripened, then very sweet. Available mid June to mid July.</p>
        <p class="variety"><span class="variety__name">Inland</span> – Very aromatic and sweet, this apricot is orange with a red blush. It has a yellow orange flesh and a round shape. Available mid June to end of July.</p>
      </div>
    </div>

    <svg class="back-band back-band--bottom" viewBox="0 0 500 160" preserveAspectRatio="none" aria-hidden="true">
      <defs>
        <linearGradient id="washBottom" x1="0" y1="0" x2="1" y2="0">
          <stop offset="0" stop-color="#ffbe45"/>
          <stop offset="1" stop-color="#f79a1e"/>
        </linearGradient>
      </defs>
      <path fill="url(#washBottom)" d="M0 40C30 30 55 46 85 36C120 24 150 42 185 32C220 22 250 40 285 30C320 20 350 36 385 28C420 20 450 34 480 26C490 24 496 26 500 28V160H0Z"/>
    </svg>
    <div class="corner-fruit" role="img" aria-label="Illustration of a whole apricot with a leaf and a halved apricot"></div>
  </section>

</body>
</html>
```